Fleeing Marisol Bay website

A very basic website using the graphics provided. The site would give the user the ability to read a description of the book, read testimonials, About the author, Read chapter 1, link to vantoro, order direct via quidlet.

```html
<!DOCTYPE html>
<html lang="en">
<head>
<meta charset="utf-8">
<title>Fleeing Marisol Bay — Daniel Harrow</title>
<link rel="stylesheet" href="https://fonts.googleapis.com/css2?family=Arimo:wght@400;700&family=Carlito:ital,wght@0,400;0,700;1,400&family=Tinos&display=swap">
<style>
:root{
  --black:#000;
  --footer:#050505;
  --gold:#f5b400;
  --white:#fff;
  --grey-text:#8a8a8a;
  --heading-grey:#777;
  --band:#444548;
  --footer-text:#b8b8b8;
  --divider:#2c2c2c;
  --link:#2a9fd8;
  --icon-grey:#9a9a9a;
}
*{margin:0;padding:0;box-sizing:border-box}
html,body{width:1200px;height:1000px;overflow:hidden;background:var(--white)}
body{position:relative;font-family:"Arimo",Arial,sans-serif}
h1,h2,h3{font-weight:400}
.abs{position:absolute}

.hero{left:0;top:0;width:1200px;height:357px;background:var(--black)}
.hero-art{left:505px;top:0;width:395px;height:305px;
  background:linear-gradient(180deg,#4f6474 0%,#2e3a42 55%,#000 100%)}
.book-title{left:450px;top:226px;color:var(--gold);font-family:"Tinos",serif;font-weight:400;line-height:1}
.book-title .small{display:block;font-size:24px}
.book-title .big{display:block;font-size:42px;margin-top:8px}
.author-name{left:452px;top:321px;color:var(--white);font-size:20px}
.name-rule{left:602px;top:325px;width:1px;height:23px;background:#777}
.author-role{left:622px;top:329px;color:var(--white);font-size:13px}
.social{left:860px;top:326px;display:flex;gap:3px}
.social span{width:16px;height:16px;border-radius:50%;background:var(--icon-grey)}

.portrait{left:278px;top:300px;width:114px;height:114px;border-radius:50%;border:3px solid var(--white);
  background:radial-gradient(circle at 50% 40%,#c9c9c9,#8f8f8f 70%,#5c5c5c)}

.about-heading{left:452px;top:402px;font-size:12.5px;color:var(--heading-grey);letter-spacing:.2px}
.about-heading b{font-weight:700}

.side-nav{left:330px;top:457px;list-style:none}
.side-nav::before{content:"";position:absolute;left:4.5px;top:6px;width:1px;height:116px;background:#bbb}
.side-nav li{position:absolute;left:0;white-space:nowrap;font-size:10.5px;color:var(--grey-text);padding-left:20px;line-height:12px}
.side-nav li::before{content:"";position:absolute;left:0;top:1px;width:10px;height:10px;border-radius:50%;border:1px solid #aaa;background:var(--white)}
.side-nav li.active{color:var(--gold);font-weight:700}
.side-nav li.active::before{background:var(--gold);border-color:var(--gold)}

.book-photo{left:452px;top:440px;width:151px;height:99px;background:linear-gradient(90deg,#2a1a10,#4a3424 50%,#1c2a34)}
.about-text{left:616px;top:438px;width:322px;font-size:9px;line-height:13px;color:var(--grey-text)}
.about-text p+p{margin-top:7px}
.read-more{left:452px;top:556px;font-size:7.5px;font-weight:700;color:#666;text-decoration:underline}

.quote-band{left:0;top:610px;width:1200px;height:87px;background:var(--band)}
.quote-mark{left:388px;top:632px;font-family:"Tinos",serif;font-size:30px;color:#888;line-height:1}
.quote-text{left:452px;top:633px;width:350px;font-family:"Carlito",sans-serif;font-style:italic;font-size:9.5px;line-height:12px;color:#ddd}
.quote-by{left:452px;top:669px;font-size:9.5px;font-weight:700;color:var(--white)}

.footer{left:0;top:697px;width:1200px;height:248px;background:var(--footer)}
.col-rule{top:730px;width:1px;height:173px;background:var(--divider)}
.footer-title{font-family:"Carlito",sans-serif;font-size:13px;font-weight:400;color:var(--gold)}
.footer-text{font-family:"Carlito",sans-serif;font-size:9.3px;line-height:12px;color:var(--footer-text)}
.feed-head{left:545px;top:764px;display:flex;align-items:center;gap:8px;font-family:"Tinos",serif;font-size:11.5px;color:#ccc}
.feed-head span{width:17px;height:17px;border-radius:50%;background:#bbb}
.tweet{left:546px;width:200px;font-family:"Carlito",sans-serif;font-size:9px;line-height:11.5px;color:#999}
.tweet a{color:var(--link);text-decoration:none}
.tweet small{font-size:7px;color:#ccc}
.order-title{left:793px;top:743px;font-family:"Carlito",sans-serif;font-size:12px;font-weight:400;color:#ddd}
.order-title b{color:var(--gold);font-weight:700}
.order-text{left:793px;top:772px;width:140px;font-family:"Carlito",sans-serif;font-size:7px;line-height:10px;color:#ddd}
.pay{top:805px;width:30px;height:20px;background:var(--white);border-radius:2px;display:flex;align-items:center;justify-content:center;font-family:"Carlito",sans-serif;font-size:7px;color:#333}

.copyright{left:278px;top:959px;font-family:"Carlito",sans-serif;font-size:7.5px;color:#888}
</style>
</head>
<body>
<header>
  <div class="abs hero"></div>
  <div class="abs hero-art" role="img" aria-label="Book cover artwork for Fleeing Marisol Bay"></div>
  <h1 class="abs book-title"><span class="small">FLEEING</span><span class="big">MARISOL BAY</span></h1>
  <div class="abs author-name">Daniel Harrow</div>
  <div class="abs name-rule"></div>
  <div class="abs author-role">Author</div>
  <div class="abs social" aria-label="Social links"><span></span><span></span><span></span><span></span></div>
  <div class="abs portrait" role="img" aria-label="Portrait of the author"></div>
</header>

<main>
  <h2 class="abs about-heading"><b>ABOUT FLEEING</b> MARISOL BAY</h2>
  <ul class="abs side-nav">
    <li class="active" style="top:0">Home</li>
    <li style="top:27px">About Book</li>
    <li style="top:49px">About Author</li>
    <li style="top:72px">Testimonial</li>
    <li style="top:94px">Read Chapter 1</li>
    <li style="top:117px">Contact</li>
  </ul>
  <div class="abs book-photo" role="img" aria-label="Photo of the printed book, front and back covers"></div>
  <div class="abs about-text">
    <p>Lorem Ipsum is simply dummy text of the printing and typesetting industry. Lorem Ipsum has been the industry's standard dummy text ever since the 1500s, when an unknown printer took a galley of type and scrambled it to make a type specimen book.</p>
    <p>Lorem Ipsum is simply dummy text of the printing and typesetting industry. Lorem Ipsum has been the industry's standard dummy text ever since the 1500s, when an unknown printer took a galley of type and scrambled it to make a type specimen book.</p>
  </div>
  <a class="abs read-more">READ MORE</a>

  <section>
    <div class="abs quote-band"></div>
    <div class="abs quote-mark">&ldquo;</div>
    <p class="abs quote-text">Lorem Ipsum is simply dummy text of the printing and typesetting industry. Lorem Ipsum has been the industry's standard dummy text ever since the 1500s</p>
    <div class="abs quote-by">By Admin</div>
  </section>
</main>

<footer>
  <div class="abs footer"></div>
  <h3 class="abs footer-title" style="left:278px;top:742px">About Author</h3>
  <div class="abs footer-text" style="left:278px;top:768px;width:225px">
    <p>Lorem Ipsum is simply dummy text of the printing and typesetting industry. Lorem Ipsum has been the industry's standard dummy text ever since the 1500s, when an unknown printer took a galley of type and scrambled it to make a type specimen book.</p>
    <p style="margin-top:12px">It has survived not only five centuries, but also the leap into electronic typesetting, remaining essentially unchanged. It was popularised in the 1960s.</p>
  </div>
  <div class="abs col-rule" style="left:514px"></div>

  <h3 class="abs footer-title" style="left:543px;top:742px">Get In Tweet</h3>
  <div class="abs feed-head"><span></span>Fleeing Marisol Bay</div>
  <p class="abs tweet" style="top:786px"><a>http://abc.marisolbay/</a>Lorem Ipsum is simply dummy text of the printing and typesetting industry - <small>2min ago</small></p>
  <p class="abs tweet" style="top:826px"><a>http://abc.marisolbay/</a>Lorem Ipsum is simply dummy text of the printing and typesetting industry - <small>2min ago</small></p>
  <div class="abs col-rule" style="left:764px"></div>

  <h3 class="abs order-title">ORDER THIS BOOK <b>NOW!</b></h3>
  <p class="abs order-text">Lorem Ipsum is simply dummy text of the printing and typesetting industry</p>
  <div class="abs pay" style="left:793px">quidlet</div>
  <div class="abs pay" style="left:831px">vantoro</div>

  <p class="abs copyright">Copyright 2014 All Right Reserved. Company Name</p>
</footer>
</body>
</html>
```